BrovaLT BIZ Card, email signature & Stationary

Professional business cards, email signatures and ms word letterhead

Target Market(s)

business owners

Industry/Entity Type

cloud hosting

Contact Information for Business Card

name title office phone number , direct line, fax email address web site

Font styles to use
Other font styles liked:
• something that compliments font in logo

```html
<!DOCTYPE html>
<html lang="en">
<head>
<meta charset="utf-8">
<title>BrovaLT Business Card</title>
<link rel="stylesheet" href="https://fonts.googleapis.com/css2?family=Arimo:wght@400;700&display=swap">
<style>
  :root {
    --stage: #2b2b30;
    --card-dark: #0d0d0d;
    --card-light: #ffffff;
    --brand-red: #e5262d;
    --ink: #222222;
    --ink-soft: #555555;
    --on-dark: #f2f2f2;
  }
  * { box-sizing: border-box; margin: 0; padding: 0; }
  html, body { width: 1200px; height: 900px; overflow: hidden; }
  body {
    background: var(--stage);
    position: relative;
    font-family: "Arimo", Arial, sans-serif;
  }
  .card {
    position: absolute;
    width: 560px;
    height: 320px;
    border-radius: 18px;
    overflow: hidden;
  }
  .card--back {
    left: 60px; top: 80px;
    background: var(--card-dark);
    display: flex; flex-direction: column; align-items: center; justify-content: center;
    gap: 24px;
  }
  .card--front {
    left: 580px; top: 500px;
    background: var(--card-light);
  }
  .brand-name {
    font-family: "Arimo", Arial, sans-serif;
    font-weight: 700;
    line-height: 1;
    letter-spacing: 0;
  }
  .card--back .brand-name { font-size: 60px; color: var(--on-dark); }
  .website { color: var(--on-dark); font-size: 17px; letter-spacing: 0.5px; }
  .card--front .brand-name {
    position: absolute; left: 44px; top: 150px;
    font-size: 40px; color: var(--ink);
  }
  .details {
    position: absolute; left: 300px; top: 44px; width: 240px;
  }
  .person-name {
    color: var(--brand-red); font-weight: 700; font-size: 19px;
    text-transform: uppercase; letter-spacing: 0.3px;
  }
  .person-title { color: var(--ink); font-size: 14px; margin-top: 3px; }
  .address { color: var(--ink-soft); font-size: 13.5px; line-height: 1.35; margin-top: 14px; }
  .contact-list { list-style: none; margin-top: 18px; }
  .contact-list li {
    display: flex; align-items: center; gap: 10px;
    color: var(--ink); font-size: 14px; line-height: 1.6;
  }
  .contact-list svg { width: 14px; height: 14px; flex: none; }
</style>
</head>
<body>
  <section class="card card--back">
    <div class="brand-name">BrovaLT</div>
    <div class="website">www.brovalt.net</div>
  </section>

  <section class="card card--front">
    <div class="brand-name">BrovaLT</div>
    <div class="details">
      <h1 class="person-name">Rowan Ellery</h1>
      <p class="person-title">Managing Director</p>
      <p class="address">The old orchard lane<br>northbridge NB4 2KX</p>
      <ul class="contact-list">
        <li>
          <svg viewBox="0 0 16 16" aria-hidden="true"><path fill="#e5262d" d="M3 1l3 3-2 2c1 2 3 4 5 5l2-2 3 3-2 3C6 15 1 10 0 3z"/></svg>
          041-310 482 657
        </li>
        <li>
          <svg viewBox="0 0 16 16" aria-hidden="true"><rect x="4" y="1" width="8" height="14" rx="1.5" fill="none" stroke="#e5262d" stroke-width="1.6"/></svg>
          052-774 190 318
        </li>
        <li>
          <svg viewBox="0 0 16 16" aria-hidden="true"><rect x="4" y="1" width="8" height="5" fill="#e5262d"/><rect x="1" y="6" width="14" height="7" rx="1" fill="#e5262d"/><rect x="4" y="10" width="8" height="5" fill="#fff" stroke="#e5262d" stroke-width="1.2"/></svg>
          013-586 247 901
        </li>
        <li>
          <svg viewBox="0 0 16 16" aria-hidden="true"><rect x="1" y="3" width="14" height="10" rx="1" fill="#e5262d"/><path d="M1.5 4l6.5 5 6.5-5" fill="none" stroke="#fff" stroke-width="1.3"/></svg>
          hello@brovalt.net
        </li>
      </ul>
    </div>
  </section>
</body>
</html>
```